Building Maintenance Flyer specialising in hot and silent pressure cleaning

Hi. I love this flyer. I would like something similar but with hot water pressure washing and building maintenance

Ferro Lane & Services provides high pressure steam cleaning and water blasting services throughout Brisbane and surrounding areas, covering the Industrial, Commercial, Strata and Residential property owners sectors.

FLS combining the cleaning power of heat with state-of-the-art silent equipment, accredited technicians and a steadfast commitment to the environment. We offer the best Prompt, Professional Service.

Fully Accredited & Certified Technicians
100% Satisfaction Guaranteed
We are a family owned and operated business and love what we do. No job is too big or too small and we take pride in our work.
All of our services are undertaken using industry leading equipment and, providing safe and superior results.

Our business is covered by 20 million full public liability insurance and we operate within strict health & safety guidelines, providing all our clients with complete peace of mind. Project plans and risk assessments can also be provided upon request.

BODY CORPORATES

BUILDING FAÇADE CLEANING

CAR PARKS – underground, single and multi level

DRIVE THRU

FOOD PRODUCTION FACILITIES CLEANING SANITISING

SHOPPING CENTRES

BIRD MANAGEMENT AND DECONTAMINATION

GENERAL MAINTENANCE

CONSTRUCTION CLEAN UPS

SPILL MANAGEMENT

CONCRETE CLEANING AND DEGRASING

CONCRETE SEALING

FACTORY CLEANING & CLEAN UP

ENVIRONMENTAL DECONTAMINATION OF HEAVY VEHICLES AND EQUIPMENT

SITE CLEANS AND RUBBISH REMOVAL

MANUFACTURING PLANTS

Target Market(s)

Facility Managers, Commercial and Industrial Property Owners, Property Managers, Schools, Restaurants,

Industry/Entity Type

Pressure Cleaning

Font styles to use
Sans Serif

Colors
0293ce
00a990
33a6d7
33b8a4

Requirements
Must have
• SILENT HOT WATER PRESSURE CLEANING
Runs up to 120 Degrees Celsius
SANITISING - Bin areas, outdoor areas, cafe's, restaurants, schools, drive thru's
Blue's and Greens to link in with our logo

```html
<!DOCTYPE html>
<html lang="en">
<head>
<meta charset="utf-8">
<title>FLS – Commercial &amp; Property Flyer</title>
<link href="https://fonts.googleapis.com/css2?family=Montserrat:wght@400;500;600;700;800&display=swap" rel="stylesheet">
<style>
  :root{
    --blue:#1f6fc4;
    --sky:#0293ce;
    --sky-soft:#33a6d7;
    --teal:#00a990;
    --teal-soft:#33b8a4;
    --teal-pale:#9fdcd2;
    --ink:#1d1d1f;
    --charcoal:#2b2b2b;
    --white:#ffffff;
    --stage:#a6a6a6;
  }
  *{box-sizing:border-box;margin:0;padding:0}
  html,body{width:1200px;height:1200px;overflow:hidden;background:var(--stage)}
  body{font-family:"Montserrat",Arial,sans-serif;position:relative}
  .flyer{position:absolute;left:40px;top:205px;width:1120px;height:790px;background:var(--white);overflow:hidden;box-shadow:0 10px 30px rgba(0,0,0,.25)}
  .flyer-shapes{position:absolute;left:0;top:0}
  .photo-cleaning{position:absolute;left:0;top:0;width:700px;height:560px;
    background:linear-gradient(135deg,#d9d9d9 0%,#8d8d8d 25%,#d8202e 45%,#7a1a22 62%,#3a3a3a 80%,#bdbdbd 100%)}
  .photo-technician{position:absolute;left:945px;top:360px;width:175px;height:430px;border-radius:88px 88px 0 0;
    background:linear-gradient(180deg,#2f5fb8 0%,#f1f1f1 24%,#e9e9e9 40%,#2a64c0 56%,#1f55a8 100%)}
  .brand{position:absolute;left:665px;top:40px;width:360px;text-align:center;
    font-weight:800;font-size:80px;color:var(--blue);letter-spacing:2px;line-height:1.1}
  .headline{position:absolute;left:615px;top:195px;width:460px;text-align:center;font-weight:700;line-height:1}
  .headline-top{display:block;font-size:36px;color:var(--ink)}
  .headline-accent{display:block;font-size:48px;color:var(--teal);margin-top:6px}
  .tagline{position:absolute;left:600px;top:305px;width:380px;text-align:center;font-size:15px;font-weight:400;color:var(--ink);line-height:1.4}
  .features{position:absolute;left:620px;top:370px;list-style:none}
  .feature{display:flex;align-items:center;gap:20px;height:58px;font-size:15px;font-weight:600;color:var(--ink);line-height:1.35;width:320px}
  .feature svg{flex:none}
  .solutions-title{position:absolute;left:48px;top:478px;font-size:36px;font-weight:800;color:var(--white);letter-spacing:-.5px}
  .solutions-swoosh{position:absolute;left:150px;top:526px}
  .solutions{position:absolute;left:40px;top:568px;display:grid;grid-template-columns:220px 210px;column-gap:18px;row-gap:10px;list-style:none}
  .solution{display:flex;align-items:center;gap:10px;color:var(--white);font-size:14px;font-weight:600;line-height:1.25;min-height:44px}
  .solution svg{flex:none}
  .badge{position:absolute;left:345px;top:345px}
  .contact{position:absolute;left:590px;top:612px;width:340px;text-align:center;color:var(--blue)}
  .social{display:flex;justify-content:center;gap:22px;margin-bottom:8px}
  .social span{width:28px;height:28px;border-radius:6px;background:var(--blue)}
  .social span:last-child{background:#d9473a}
  .phone{display:flex;align-items:center;justify-content:center;gap:8px;font-size:40px;font-weight:700;letter-spacing:1px;line-height:1.15}
  .contact-line{display:flex;align-items:center;justify-content:center;gap:10px;font-weight:600;margin-top:4px}
  .contact-web{font-size:21px}
  .contact-mail{font-size:16px}
</style>
</head>
<body>
<section class="flyer">
  <div class="photo-cleaning" role="img" aria-label="Photo of a technician pressure washing a red vehicle with hot water spray"></div>
  <svg class="flyer-shapes" width="1120" height="790" viewBox="0 0 1120 790">
    <defs>
      <linearGradient id="skyFade" x1="0" y1="0" x2="1" y2="0">
        <stop offset="0" stop-color="#ffffff"/>
        <stop offset="0.55" stop-color="#e6f6fc"/>
        <stop offset="1" stop-color="#5cc4ec"/>
      </linearGradient>
      <linearGradient id="panelBlue" x1="0" y1="0" x2="1" y2="1">
        <stop offset="0" stop-color="#2068c0"/>
        <stop offset="1" stop-color="#0f84cf"/>
      </linearGradient>
    </defs>
    <path class="band-teal" d="M590 0 L1120 0 L1120 790 L480 790 C470 600 460 450 500 320 C530 200 560 90 590 0 Z" fill="var(--teal)"/>
    <path class="band-dark" d="M640 0 L1120 0 L1120 790 L520 790 C510 610 500 460 535 330 C565 210 600 90 640 0 Z" fill="var(--charcoal)"/>
    <path class="field-white" d="M690 0 L1120 0 L1120 790 L560 790 C550 620 545 470 575 345 C605 225 645 100 690 0 Z" fill="var(--white)"/>
    <path class="panel-edge" d="M0 420 C120 340 300 320 420 360 C520 400 560 560 545 790 L0 790 Z" fill="var(--teal-pale)"/>
    <path class="panel-blue" d="M0 428 C110 352 290 336 400 374 C490 412 525 560 505 790 L0 790 Z" fill="url(#panelBlue)"/>
    <path class="field-sky" d="M562 600 C700 596 900 572 1120 502 L1120 790 L560 790 C572 720 572 660 562 600 Z" fill="url(#skyFade)"/>
    <path class="sweep-line" d="M540 600 C700 596 900 572 1120 500" fill="none" stroke="var(--teal)" stroke-width="10"/>
    <path class="edge-line" d="M552 520 C575 620 575 700 560 790" fill="none" stroke="var(--teal)" stroke-width="14"/>
  </svg>
  <div class="photo-technician" role="img" aria-label="Photo of a smiling technician in blue overalls giving a thumbs up"></div>

  <div class="brand">FLS</div>
  <h1 class="headline"><span class="headline-top">ALL COMMERCIAL &amp;</span><span class="headline-accent">PROPERTY</span></h1>
  <p class="tagline">FLS – servicing Southeast's Commercial<br>&amp; Industrial sector 24/7</p>

  <ul class="features">
    <li class="feature">
      <svg width="44" height="44" viewBox="0 0 46 46"><circle cx="23" cy="23" r="19" fill="none" stroke="#1d1d1f" stroke-width="3"/><text x="23" y="29" text-anchor="middle" font-family="Montserrat,sans-serif" font-weight="800" font-size="16" fill="#1d1d1f">24</text></svg>
      <span>We operate 24/7, 7 days a week</span>
    </li>
    <li class="feature">
      <svg width="44" height="44" viewBox="0 0 46 46"><path d="M34 6 L22 24" stroke="#1d1d1f" stroke-width="3" fill="none"/><path d="M14 22 L28 30 L22 40 L6 34 Z" fill="none" stroke="#1d1d1f" stroke-width="2.5"/><circle cx="36" cy="34" r="3" fill="none" stroke="#1d1d1f" stroke-width="2"/><circle cx="40" cy="41" r="2" fill="none" stroke="#1d1d1f" stroke-width="2"/></svg>
      <span>SILENT HOT WATER pressure cleaning 120 degrees</span>
    </li>
    <li class="feature">
      <svg width="44" height="44" viewBox="0 0 46 46"><circle cx="23" cy="23" r="13" fill="none" stroke="#1d1d1f" stroke-width="3"/><g stroke="#1d1d1f" stroke-width="2.5"><path d="M23 4v6M23 36v6M4 23h6M36 23h6M10 10l4 4M32 32l4 4M36 10l-4 4M10 36l4-4"/></g></svg>
      <span>COVID-19 Trained</span>
    </li>
  </ul>

  <svg class="badge" width="120" height="120" viewBox="0 0 130 130" role="img" aria-label="Satisfaction guarantee seal">
    <circle cx="65" cy="65" r="62" fill="#c9ced6" stroke="#eef0f3" stroke-width="4"/>
    <circle cx="65" cy="65" r="40" fill="#1b2a45"/>
  </svg>

  <h2 class="solutions-title">Solutions For:</h2>
  <svg class="solutions-swoosh" width="220" height="30" viewBox="0 0 220 30"><path d="M0 28 C60 8 140 2 220 6 C140 8 70 14 0 28 Z" fill="#fff"/></svg>
  <ul class="solutions">
    <li class="solution"><svg width="22" height="22" viewBox="0 0 22 22"><circle cx="11" cy="11" r="9" fill="none" stroke="#fff" stroke-width="2"/></svg>COVID-19 Infection Control</li>
    <li class="solution"><svg width="22" height="22" viewBox="0 0 22 22"><path d="M2 18 L6 8 L11 14 L16 6 L20 18 Z" fill="#fff"/></svg>Common Area Cleaning</li>
    <li class="solution"><svg width="22" height="22" viewBox="0 0 22 22"><rect x="4" y="2" width="14" height="18" fill="#fff"/></svg>Building Maintenance</li>
    <li class="solution"><svg width="22" height="22" viewBox="0 0 22 22"><path d="M3 18 C6 8 16 8 19 18 Z" fill="#fff"/></svg>Bird waste removal</li>
    <li class="solution"><svg width="22" height="22" viewBox="0 0 22 22"><path d="M4 6 H18 L16 20 H6 Z" fill="#fff"/></svg>Bin Cleaning &amp; Sanitisation</li>
    <li class="solution"><svg width="22" height="22" viewBox="0 0 22 22"><rect x="5" y="4" width="12" height="16" fill="none" stroke="#fff" stroke-width="2"/><path d="M3 4 H19" stroke="#fff" stroke-width="2"/></svg>Mould &amp; Mildew removal</li>
    <li class="solution"><svg width="22" height="22" viewBox="0 0 22 22"><circle cx="6" cy="16" r="4" fill="#fff"/><path d="M8 14 L20 3" stroke="#fff" stroke-width="2"/></svg>Concrete Cleaning &amp; Sealing</li>
    <li class="solution"><svg width="22" height="22" viewBox="0 0 22 22"><path d="M11 2 C15 8 17 11 17 14 A6 6 0 0 1 5 14 C5 11 7 8 11 2 Z" fill="#fff"/></svg>Oil and Grease elimination</li>
  </ul>

  <div class="contact">
    <div class="social"><span></span><span></span><span></span></div>
    <div class="phone"><svg width="28" height="28" viewBox="0 0 24 24"><path d="M6.6 10.8a15 15 0 0 0 6.6 6.6l2.2-2.2a1 1 0 0 1 1-.25 11.4 11.4 0 0 0 3.6.57 1 1 0 0 1 1 1V20a1 1 0 0 1-1 1A17 17 0 0 1 3 4a1 1 0 0 1 1-1h3.5a1 1 0 0 1 1 1c0 1.250.2 2.45.57 3.6a1 1 0 0 1-.25 1z" fill="var(--blue)"/></svg>1-555-0148</div>
    <div class="contact-line contact-web"><svg width="22" height="22" viewBox="0 0 24 24"><circle cx="12" cy="12" r="10" fill="none" stroke="var(--blue)" stroke-width="2"/><path d="M2 12h20M12 2c4 4 4 16 0 20M12 2c-4 4-4 16 0 20" fill="none" stroke="var(--blue)" stroke-width="1.5"/></svg>www.ferrolane-fls.com</div>
    <div class="contact-line contact-mail"><svg width="20" height="15" viewBox="0 0 22 16"><rect x="1" y="1" width="20" height="14" fill="none" stroke="var(--blue)" stroke-width="2"/><path d="M1 1 L11 9 L21 1" fill="none" stroke="var(--blue)" stroke-width="2"/></svg>hello@ferrolane-fls.com</div>
  </div>
</section>
</body>
</html>
```